Business Card design for amazing new Dental Office

Please read this brief closely!

Our client is a modern new dental office/
They love their new logo.
Now it's time to create a business card for them.

It should be a two sided card:
Side one should have the logo and name and maybe a color background or design.
Side two should have all the contact information which is here:

Elliot Brannick, D.D.S
General and Cosmetic Dentistry
4187 W. Pinecrest Avenue
Ventura, CA 93011
(805) 912-4386
drelliot@bluefernsmiles-example.com
www.bluefernsmiles-example.com

Feel free to arrange that info as you like and to style both sides of the card according to your creativity. This is a chance for you to show your design skills!

Client is open to font choices and is looking for a style that is amazing and premium. Colors can be selected from the logo, or any variation of those.

You will not win this contest with a less than beautiful card design so please feel free to make multiple submissions.

Logo files attached and please message me with any questions.
Thanks!

Target Market(s)

Families and Professionals seeking dental services

Industry/Entity Type

Dental

Contact Information for Business Card

Logo, style, contact info as per the brief

Font styles to use
Sans Serif

Requirements
Must have
• Client's logo and contact details as per brief
Nice to have
• Unique style reflecting high end dental clinic near the beach
Should not have
• Must not look like a template

```html
<!DOCTYPE html>
<html lang="en">
<head>
<meta charset="utf-8">
<title>Blue Fern Smiles – Business Card</title>
<link rel="stylesheet" href="https://fonts.googleapis.com/css2?family=Didact+Gothic&family=Montserrat:wght@700&display=swap">
<style>
  :root {
    --backdrop: #2a2a2b;
    --card-light: #ffffff;
    --card-light-shade: #eef0f1;
    --card-dark: #1e1a1a;
    --gold: #b6a23a;
    --copper: #d98d3e;
    --ink: #3a3a3a;
    --brand-grey: #8f9396;
    --brand-light: #c9cccf;
    --teal: #3fb6c4;
  }
  * { box-sizing: border-box; margin: 0; padding: 0; }
  html, body {
    width: 1200px; height: 900px; overflow: hidden;
    background: var(--backdrop);
    font-family: "Didact Gothic", sans-serif;
  }
  .canvas { position: relative; width: 1200px; height: 900px; }

  .card {
    position: absolute;
    width: 630px; height: 360px;
    border-radius: 26px;
    box-shadow: 0 18px 40px rgba(0,0,0,.45);
    overflow: hidden;
  }

  /* Contact side */
  .card--contact {
    left: 70px; top: 70px;
    background: linear-gradient(135deg, var(--card-light-shade) 0%, var(--card-light) 45%, var(--card-light) 100%);
  }
  .brand {
    position: absolute;
    display: flex; align-items: center; gap: 10px;
    font-family: "Didact Gothic", sans-serif;
    letter-spacing: .12em;
    text-transform: uppercase;
    white-space: nowrap;
  }
  .brand__dot { border-radius: 50%; background: var(--teal); flex: none; }
  .card--contact .brand { right: 40px; top: 46px; font-size: 26px; color: var(--brand-grey); }
  .card--contact .brand__dot { width: 14px; height: 14px; }

  .doctor { position: absolute; left: 44px; top: 146px; }
  .doctor__name {
    font-family: "Montserrat", sans-serif; font-weight: 700;
    color: var(--gold); font-size: 24px; letter-spacing: .01em;
  }
  .doctor__role { color: var(--ink); font-size: 20px; margin-top: 4px; }

  .contact-list { position: absolute; left: 44px; top: 234px; list-style: none; }
  .contact-list li {
    display: flex; align-items: center; gap: 10px;
    color: var(--ink); font-size: 17px; line-height: 25px;
  }
  .icon { width: 16px; height: 16px; flex: none; fill: var(--copper); }

  .divider {
    position: absolute; left: 44px; right: 44px; top: 314px;
    height: 1px; background: var(--gold);
  }
  .address {
    position: absolute; left: 44px; top: 322px;
    display: flex; align-items: center; gap: 10px;
    color: var(--ink); font-size: 17px; line-height: 22px;
  }

  /* Brand side */
  .card--brand {
    left: 500px; top: 480px;
    background: var(--card-dark);
  }
  .card--brand .brand {
    left: 50%; top: 50%; transform: translate(-50%, -50%);
    font-size: 38px; color: var(--brand-light);
  }
  .card--brand .brand__dot { width: 20px; height: 20px; }
</style>
</head>
<body>
<main class="canvas">

  <section class="card card--contact" aria-label="Contact side">
    <div class="brand"><span class="brand__dot"></span>Blue Fern Smiles</div>

    <div class="doctor">
      <h1 class="doctor__name">Elliot Brannick, D.D.S</h1>
      <p class="doctor__role">General and Cosmetic Dentistry</p>
    </div>

    <ul class="contact-list">
      <li>
        <svg class="icon" viewBox="0 0 16 16" aria-hidden="true"><path d="M3 2h3l1.5 3.5-2 1.2a8 8 0 0 0 3.8 3.8l1.2-2L14 10v3a1 1 0 0 1-1 1A11 11 0 0 1 2 3a1 1 0 0 1 1-1z"/></svg>
        (805) 912-4386
      </li>
      <li>
        <svg class="icon" viewBox="0 0 16 16" aria-hidden="true"><circle cx="8" cy="8" r="7" fill="none" stroke="var(--copper)" stroke-width="1.6"/><path d="M1 8h14M8 1c-3 3.5-3 10.5 0 14M8 1c3 3.5 3 10.5 0 14" fill="none" stroke="var(--copper)" stroke-width="1.2"/></svg>
        www.bluefernsmiles-example.com
      </li>
      <li>
        <svg class="icon" viewBox="0 0 16 16" aria-hidden="true"><rect x="1" y="3" width="14" height="10" rx="1.5"/><path d="M2 4l6 5 6-5" fill="none" stroke="#fff" stroke-width="1.3"/></svg>
        drelliot@bluefernsmiles-example.com
      </li>
    </ul>

    <div class="divider"></div>

    <p class="address">
      <svg class="icon" viewBox="0 0 16 16" aria-hidden="true"><path d="M8 1a5 5 0 0 0-5 5c0 4 5 9 5 9s5-5 5-9a5 5 0 0 0-5-5zm0 7a2 2 0 1 1 0-4 2 2 0 0 1 0 4z"/></svg>
      4187 W. Pinecrest Avenue, Ventura, CA 93011
    </p>
  </section>

  <section class="card card--brand" aria-label="Brand side">
    <div class="brand"><span class="brand__dot"></span>Blue Fern Smiles</div>
  </section>

</main>
</body>
</html>
```